Looking for label design for pet health products (antimicrobial spray)

We are a start up company based in Singapore. We are manufacturing and selling antimicrobial spray for pets. Our product brand name is LeafOpal. The spray is mainly useful for cuts, sores, bacterial and fungal skin infections, wounds, dermatitis.The antimicrobial spray contains colloidal silver with Neem herbal extract. This product is free from synthetic chemicals, it is safe for internal and external use.

The target customers are pet owners. The means of sales would be e-commerce websites as well as retail stores. Primary market is Singapore and Asia. Label should be attractive to pet owners.

The label size of 15 cm in length and 7 cm in height is expected. The label is to be placed on amber colored plastic bottles of around 250 ml volume. The maximum number of colors should be three.

Industry/Entity Type

It Company

```html
<!DOCTYPE html>
<html lang="en">
<head>
<meta charset="utf-8">
<title>LeafOpal – Antimicrobial Spray Label</title>
<link rel="stylesheet" href="https://fonts.googleapis.com/css2?family=Oswald:wght@500;700&display=swap">
<style>
  :root {
    --page: #e6e6e6;
    --label-white: #ffffff;
    --label-blue: #c4e6f9;
    --brand-green: #1b5c38;
    --ribbon-red: #d0202a;
    --badge-blue: #1f78c4;
    --ink-navy: #13233a;
    --art-brown: #a0693f;
    --art-cream: #f3e9dc;
  }
  html, body {
    margin: 0;
    width: 1200px;
    height: 1200px;
    overflow: hidden;
    background: var(--page);
    font-family: "Oswald", sans-serif;
  }
  .label {
    position: absolute;
    left: 50px;
    top: 345px;
    width: 1100px;
    height: 510px;
    box-sizing: border-box;
    border: 14px solid var(--label-white);
    background: var(--label-blue);
    box-shadow: 0 6px 14px rgba(0,0,0,0.25);
  }
  .label__frame {
    position: absolute;
    inset: 0;
  }
  .mascot-art {
    position: absolute;
    left: 444px;
    top: 23px;
    width: 184px;
    height: 121px;
    border-radius: 60px 60px 20px 20px;
    background: radial-gradient(circle at 50% 55%, var(--art-cream) 0 35%, var(--art-brown) 75%);
  }
  .brand-name {
    position: absolute;
    left: 0;
    right: 0;
    top: 140px;
    margin: 0;
    text-align: center;
    font-weight: 700;
    font-size: 112px;
    line-height: 1;
    color: var(--brand-green);
  }
  .tagline-band {
    position: absolute;
    left: 352px;
    top: 296px;
    width: 369px;
    height: 56px;
    background: var(--ribbon-red);
    color: var(--label-white);
    font-weight: 500;
    font-size: 30px;
    line-height: 56px;
    text-align: center;
    letter-spacing: 0.5px;
  }
  .claim-badge {
    position: absolute;
    left: 160px;
    top: 280px;
    width: 148px;
    height: 148px;
    border-radius: 50%;
    background: var(--badge-blue);
    color: var(--label-white);
    display: flex;
    flex-direction: column;
    align-items: center;
    justify-content: center;
    line-height: 1;
    text-align: center;
  }
  .claim-badge__big { font-weight: 700; font-size: 30px; }
  .claim-badge__small { font-weight: 500; font-size: 14px; margin: 4px 0; }
  .claim-badge__mid { font-weight: 700; font-size: 24px; }
  .uses {
    position: absolute;
    left: 0;
    right: 0;
    top: 384px;
    margin: 0;
    text-align: center;
    font-weight: 500;
    font-size: 17px;
    line-height: 26px;
    color: var(--ink-navy);
  }
</style>
</head>
<body>
  <section class="label">
    <svg class="label__frame" width="1072" height="482" viewBox="0 0 1072 482" aria-hidden="true">
      <g fill="none" stroke="#ffffff" stroke-width="2">
        <path d="M430 55 H53 V466 H1019 V55 H680"/>
        <path d="M430 69 H67 V452 H1005 V69 H680"/>
      </g>
    </svg>

    <div class="mascot-art" role="img" aria-label="Illustration of a beagle puppy peeking over the brand name"></div>

    <h1 class="brand-name">LeafOpal</h1>

    <div class="tagline-band">THE ANTIMICROBIAL SPRAY</div>

    <div class="claim-badge">
      <span class="claim-badge__big">FREE</span>
      <span class="claim-badge__small">FROM SYNTHETIC</span>
      <span class="claim-badge__mid">CHEMICALS</span>
    </div>

    <p class="uses">THE SPRAY IS MAINLY USEFUL FOR CUTS, SORES,<br>BACTERIAL AND FUNGAL SKIN INFECTIONS, WOUNDS, DERMATITIS</p>
  </section>
</body>
</html>
```